Refinery Service Website (Wholesale) – Luxurious Landing Pages & Industry Hub

We are seeking talented designers to create a luxurious and professional redesign for the wholesale section of our refinery service website, Brightwell VKS. Our current refinery page (https://brightwellvks.example/refinery/) and dental landing page (https://brightwellvks.example/refinery/dental-gold/) provide functional starting points with existing content (words, sections, trust badges, and video placeholders) that must be retained and enhanced with a sophisticated, high-end aesthetic. We serve high-net-worth wholesale clients across industries such as dental practices, mortuaries, estate attorneys, dentists, pawnshops, jewelry stores, and financial advisors. The project includes designing a revamped main wholesale landing page, individual landing pages for each industry with specific sections, and a central hub page to showcase these industries in an SEO-friendly and user-focused way, all while elevating the design to a luxurious standard.

Project Overview
Our refinery service specializes in precious metals and serves a variety of industries through wholesale access. We want the wholesale section of our website to exude sophistication and exclusivity while preserving and enhancing the existing content on our pages. Currently:
• Our refinery page (https://brightwellvks.example/refinery/) provides a basic overview of our services with text, sections, and trust badges, but it lacks visual appeal and a high-end feel.
• Our dental landing page (https://brightwellvks.example/refinery/dental-gold/) targets dental professionals with relevant messaging, sections, and content, but it also feels utilitarian and could benefit from a more elegant design, improved layout, and stronger calls-to-action.
Designers must use the existing words, sections, trust badges, and video placeholders from these pages as a foundation, enhancing them with a luxurious redesign and adding the additional sections specified below. We admire the clean and professional look of https://www.tolvenmetals.example/, but we aim to elevate our design with a more luxurious and exclusive feel to attract discerning wholesale clients. The redesign will involve:
1 Main Wholesale Landing Page: A complete overhaul of our current refinery page into a luxurious and professional entry point, retaining and enhancing existing content while improving the overall design.
2 Industry-Specific Landing Pages: A dedicated landing page for each of the following industries: dental practices, mortuaries, estate attorneys, dentists, pawnshops, jewelry stores, and financial advisors. Each page must retain and enhance existing content (where applicable) and include specific sections (detailed below) to build trust, provide information, and encourage engagement.
3 Industry Hub Page: A central page that showcases all the industries we serve in a visually appealing and SEO-optimized manner, acting as a gateway to each industry-specific landing page.
Our website is built on WordPress using the Bricks Builder, so design submissions should be provided in HTML, CSS, or as a Figma file for seamless integration. The design must be responsive, visually striking, and optimized for usability across all devices (desktop, tablet, mobile).
Project Scope
We are looking for design submissions that include:
• Main Wholesale Landing Page: A redesigned version of our current refinery page (https://brightwellvks.example/refinery/), transformed into a luxurious and professional entry point for our wholesale services. The new design must retain the existing words, sections, trust badges, and any video placeholders, enhancing them with a high-end aesthetic while improving layout and engagement.
• Industry-Specific Landing Pages: A dedicated landing page for each of the following industries: dental practices, mortuaries, estate attorneys, dentists, pawnshops, jewelry stores, and financial advisors. Each page must:
◦ Retain and enhance existing content (words, sections, trust badges, video placeholders) from pages like our dental landing page (https://brightwellvks.example/refinery/dental-gold/) as a reference, adapting it for each industry. For industries without existing pages, mirror the structure and content style of the dental page while tailoring the messaging and visuals.
◦ Include the following additional sections to enhance functionality and trust:
Trust Badges: A section displaying trust signals (e.g., certifications, accreditations, years in business) to build credibility with visitors. Include placeholders for 4–6 badges/icons, enhancing any existing badges from our current pages.
Testimonials: A section featuring 3–5 customer testimonials with placeholders for quotes, names, and industries (e.g., “Dr. Carl Bevin, Dental Practice Owner”). If testimonials exist on current pages, enhance their presentation.
Contact Information: A clearly visible section with contact details (e.g., phone number, email, address) styled to match the luxurious aesthetic, improving any existing contact info presentation.
Contact Fillout Form: A user-friendly form for inquiries, including fields for name, email, industry, and message, with a professional design that encourages submissions, enhancing any existing forms.
Shipping Information: A section detailing shipping instructions and processes (e.g., how to send materials for refining), presented clearly and concisely, building on any existing shipping details.
Summary Service Bullet Points: A concise list of 5–7 key services or benefits tailored to the specific industry (e.g., “Fast turnaround for dental scrap” for dental pages, “Secure handling for jewelry inventory” for jewelers), improving any existing bullet points.
Video: Shipping Instructions: A placeholder for a video explaining how to ship materials to us, styled with a play button and a luxurious frame, enhancing any existing video placeholders.
Video: How Our Refinery Works: A placeholder for a video detailing our refining process, designed to match the aesthetic of the page, enhancing any existing video placeholders.
Video: Who We Are: A placeholder for a video introducing our company and values, presented in an elegant and professional manner, enhancing any existing video placeholders.
◦ Include tailored messaging and design elements that resonate with the specific industry (e.g., dental tools and scrap refining benefits for dental pages, elegant estate visuals for attorneys, jewelry displays for jewelers).
◦ Maintain a cohesive design that ties back to the overall luxurious aesthetic of the wholesale section.
• Industry Hub Page: A central hub page that showcases all the industries we serve in an SEO-friendly and visually engaging way. This page should include:
◦ A grid, carousel, or categorized layout featuring each industry with a concise description or tagline (e.g., “Dental Practices: Turn Scrap into Profit”).
◦ Links to each industry-specific landing page for easy navigation.
◦ Design elements that encourage exploration (e.g., hover effects, icons, or visuals representing each industry).
◦ SEO optimization through keyword-rich headings, meta-friendly layouts, and content areas that naturally incorporate industry terms.
• SEO and User Engagement Focus: The design should balance aesthetics with functionality, ensuring that both the hub page and individual landing pages are optimized for search engines (e.g., through clear headings, meta-friendly layouts) and capture user attention with compelling calls-to-action (e.g., “Discover Refinery Solutions for Your Dental Practice” or “Maximize Value for Your Jewelry Inventory”).
Design Requirements
• Aesthetic: Luxurious, elegant, and professional, with a focus on high-net-worth wholesale clients. The current designs (https://brightwellvks.example/refinery/ and https://brightwellvks.example/refinery/dental-gold/) are too basic and functional; we want a high-end look that conveys prestige and trust, using elements like deep golds, silvers, blacks, or whites to evoke luxury while enhancing existing content.
• Typography: Clean, modern, and sophisticated fonts that enhance readability and align with a high-end brand image, improving upon existing typography.
• Imagery: Incorporate placeholders for high-quality imagery relevant to each industry (e.g., dental tools, jewelry displays, legal documents). No stock images required in submissions—just placeholders. Retain and enhance any existing imagery placeholders from our current pages.
• Video Placeholders: Video sections (for shipping instructions, how the refinery works, and who we are) should include placeholders with play buttons and elegant frames that match the luxurious aesthetic, enhancing any existing video placeholders on our current pages.
• Responsiveness: The design must be fully responsive and look great on desktop, tablet, and mobile devices.
• SEO Optimization: The layout should support SEO best practices, such as clear heading structures (H1, H2, etc.), alt-text-friendly image placeholders, and keyword-rich content areas for each industry, building on existing content for SEO purposes.
• Deliverables Format: Submissions should include design files in HTML, CSS, or Figma format, ready for integration into WordPress with Bricks Builder.

Submission Guidelines
We invite designers to submit their concepts based on the following:
• A mockup of the redesigned main wholesale landing page, improving upon our current refinery page (https://brightwellvks.example/refinery/), retaining and enhancing existing words, sections, trust badges, and video placeholders with a luxurious aesthetic.
• A mockup of the industry hub page showcasing all the industries we serve (dental practices, mortuaries, estate attorneys, dentists, pawnshops, jewelry stores, financial advisors).
• At least two examples of industry-specific landing pages (e.g., one for dental practices, improving upon our current dental page (https://brightwellvks.example/refinery/dental-gold/), and one for jewelry stores), showing how the design retains and enhances existing content, incorporates all required sections (trust badges, testimonials, contact info, contact form, shipping info, service bullet points, and video placeholders), and tailors messaging to each audience.
• A brief explanation of your design choices, including how they enhance SEO, tailor messaging for each industry, incorporate and enhance existing content, include the required sections, and align with the luxurious and professional aesthetic we’re seeking.
• Files in HTML, CSS, or Figma format to demonstrate how the design can be implemented.

Judging Criteria
Submissions will be evaluated based on:
• Alignment with the luxurious and professional aesthetic described, significantly improving upon our current designs (https://brightwellvks.example/refinery/ and https://brightwellvks.example/refinery/dental-gold/) while retaining and enhancing existing content.
• Effective retention and enhancement of existing words, sections, trust badges, and video placeholders from our current pages, seamlessly integrating them into the new design.
• Inclusion and effective design of all required sections (trust badges, testimonials, contact info, contact form, shipping info, service bullet points, and video placeholders) on the industry-specific landing pages.
• Creativity and effectiveness in tailoring messaging and visuals for each industry-specific landing page.
• Usability and visual appeal of the industry hub page, including its potential to improve SEO and engage users.
• Suitability for the target audience (high-net-worth wholesale clients in dental, mortuary, legal, pawnshop, jewelry, and financial sectors).
• Compatibility with WordPress and Bricks Builder (based on the format of deliverables).

Additional Notes
• We are open to creative interpretations of “luxury” and encourage designers to think outside the box while maintaining professionalism. Use our current pages as a foundation for content and structure, enhancing and building upon them rather than replacing them entirely.
• The industry hub page should feel intuitive and encourage exploration, potentially using layouts like a grid, carousel, or categorized sections with hover effects.
• Each industry-specific landing page should include a unique value proposition (e.g., “Streamline Your Dental Scrap Refining Process” or “Maximize Value for Your Jewelry Inventory”) to capture attention, building on the clarity of our current dental page but with a more luxurious presentation and all required sections.
• We will provide feedback during the contest and may request revisions from top submissions.

About Us
Brightwell VKS is a leading refinery service provider specializing in precious metals, offering wholesale solutions to a wide range of industries such as dental, jewelry, and legal sectors. Our goal is to create a luxurious online presence that reflects the high value we provide to our clients.
We look forward to seeing your creative designs and how you can bring our vision of a luxurious, industry-focused wholesale section to life!

```html
<!DOCTYPE html>
<html lang="en">
<head>
<meta charset="utf-8">
<title>Refinery Process – Brightwell Precious Metals Refineries</title>
<link rel="stylesheet" href="https://fonts.googleapis.com/css2?family=Jost:wght@400;500;600;700&display=swap">
<style>
:root{
  --ink:#1c1b1b;
  --text:#3a3a3a;
  --muted:#7a7a7a;
  --line:#d9d9d9;
  --field:#efefef;
  --paper:#ffffff;
  --mist:#f3f3f3;
  --night:#221f1f;
  --night-2:#2b2828;
  --gold:#e4b75c;
  --gold-soft:#f1d79e;
  --accent:#4f7cff;
}
*{box-sizing:border-box;margin:0;padding:0}
html,body{width:1200px;height:4587px;overflow:hidden}
body{position:relative;background:var(--paper);font-family:"Jost",sans-serif;color:var(--text)}
.abs{position:absolute}
.center{left:0;right:0;text-align:center}
h1,h2,h3{color:var(--ink);font-weight:500}

/* header */
.topline{top:0;left:0;width:1200px;height:18px;background:#ececec;border-bottom:1px solid var(--line)}
.header{top:18px;left:0;width:1200px;height:42px;border-bottom:1px solid var(--line)}
.brand{display:flex;align-items:center;gap:8px;font-size:12px;letter-spacing:.04em;color:var(--ink)}
.brand .dot{width:14px;height:14px;border-radius:50%;background:var(--ink)}
.search{top:7px;left:714px;width:185px;height:27px;border:1px solid #bdbdbd;border-radius:14px;font-size:7px;color:#888;padding:9px 12px}
.icon{display:block}
.callbtn{top:6px;left:977px;width:29px;height:29px;border-radius:8px;background:var(--accent);display:flex;align-items:center;justify-content:center}
.nav{top:60px;left:0;width:1200px;height:24px}
.nav a{position:absolute;top:5px;font-size:10px;color:var(--ink);text-decoration:none;transform:translateX(-50%);font-weight:500}
.nav .badge{position:absolute;top:-2px;right:-6px;width:5px;height:5px;border-radius:50%;background:var(--ink)}

/* hero */
.hero{top:84px;left:0;width:1200px;height:456px;background:var(--paper);overflow:hidden;border-bottom:1px solid var(--line)}
.hero-media{position:absolute;inset:0;clip-path:polygon(520px 0,1079px 0,458px 456px,0 456px);
  background:linear-gradient(100deg,rgba(255,255,255,1) 38%,rgba(255,255,255,0) 55%),
  radial-gradient(ellipse at 700px 150px,#ffd86a 0,#f39b1f 18%,#b5440b 34%,#2a1208 55%,#5a5a5a 80%,#bdbdbd 100%)}
.hero-title{top:198px;left:183px;font-size:76px;line-height:.9;font-weight:500;color:var(--ink);letter-spacing:-.01em}

/* section heads */
.rule-orn{width:40px;height:2px;background:var(--gold);margin:0 auto}
.about{top:540px;left:0;width:1200px;height:496px;background:var(--mist)}
.copy{font-size:9.6px;line-height:13px;color:var(--text)}
.copy p{margin-bottom:10px}

.video{top:945px;left:192px;width:816px;height:431px;border-radius:25px;overflow:hidden;
  background:radial-gradient(ellipse at 50% 55%,#f4c24a 0,#b97a12 22%,#4a3212 45%,#161310 75%,#0b0a09 100%)}
.play{position:absolute;left:346px;top:153px;width:125px;height:125px;border-radius:50%;background:#fff;display:flex;align-items:center;justify-content:center}

.gems{top:1716px;left:0;width:1200px;height:160px}
.gem{position:absolute;width:142px;height:114px;clip-path:polygon(18% 0,82% 0,100% 30%,50% 100%,0 30%)}
.gem-label{position:absolute;top:134px;width:160px;font-size:7.5px;letter-spacing:.02em;text-align:center;color:#555;transform:translateX(-50%)}

/* middle man */
.middle{top:1931px;left:0;width:1200px;height:609px;background:var(--night)}
.middle-photo{position:absolute;left:0;top:0;width:600px;height:609px;
  background:radial-gradient(circle at 215px 450px,#ffb347 0,#e0621a 8%,#5b4c44 20%,#8f8f8f 45%,#cfcfcf 75%,#e6e6e6 100%)}
.middle h2{color:#fff;font-size:20px}
.middle .hr{left:726px;width:349px;height:1px;background:#8a7446}
.middle .copy{color:#d8d8d8;font-size:11px;line-height:20px}
.scroll-track{left:1168px;width:2px;background:#5a5656}
.coin{position:absolute;top:2388px;width:85px;height:85px;border-radius:50%}
.coin.gold{background:radial-gradient(circle at 38% 32%,#fbe6a2 0,#d7a93f 45%,#8d6516 100%)}
.coin.silver{background:radial-gradient(circle at 38% 32%,#ffffff 0,#c9c9c9 45%,#767676 100%)}

/* registration */
.reg-title{font-size:40px;font-weight:500}
.step{position:absolute;top:2761px;width:42px;height:42px;border-radius:50%;background:#eaeaea;display:flex;align-items:center;justify-content:center;transform:translateX(-50%)}
.step.active{background:var(--ink)}
.step-label{position:absolute;top:2822px;width:110px;font-size:8.5px;line-height:12px;text-align:center;color:var(--ink);transform:translateX(-50%);font-weight:500}
.dash{position:absolute;top:2782px;height:0;border-top:1px dashed #9a9a9a}
.form-label{position:absolute;font-size:8px;color:var(--ink);font-weight:500}
.form-label b{color:#d34a4a;font-weight:500}
.field{position:absolute;height:38px;background:var(--field);border-radius:3px}
.continue{top:3185px;left:906px;width:96px;height:28px;border-radius:14px;background:var(--ink);color:#fff;font-size:9px;display:flex;align-items:center;justify-content:center;gap:6px}

/* industries */
.card{position:absolute;top:3370px;width:263px;height:336px;overflow:hidden}
.card .shade{position:absolute;inset:0;background:linear-gradient(180deg,rgba(0,0,0,0) 60%,rgba(0,0,0,.55) 100%)}
.card span{position:absolute;left:30px;bottom:26px;color:#fff;font-size:14px;font-weight:500}
.arrow{position:absolute;top:3690px;width:32px;height:32px;border-radius:50%;background:var(--ink);display:flex;align-items:center;justify-content:center;transform:translateX(-50%)}
.arrow.hot{background:var(--gold)}
.pager{position:absolute;top:3751px;height:3px;width:43px;background:#cfcfcf}
.pager.on{background:var(--ink)}

.perk{position:absolute;top:3854px;width:246px;height:133px;border-radius:18px;padding:44px 26px 0;color:#fff;overflow:hidden}
.perk.dark{background:var(--night-2)}
.perk.goldcard{background:linear-gradient(100deg,#f3dcab 0,#e8c06c 60%,#d9a84c 100%);color:var(--ink)}
.perk h3{font-size:12.5px;font-weight:600;color:inherit}
.perk p{font-size:7px;margin-top:4px;opacity:.8}
.perk .cta{position:absolute;left:26px;top:107px;font-size:7px;font-weight:600;letter-spacing:.04em}
.perk svg.mark{position:absolute;right:22px;top:88px}

/* footer */
.footer{top:4075px;left:0;width:1200px;height:332px;background:var(--night);color:#eee}
.fcol{position:absolute;top:62px;font-size:7px;line-height:16px}
.fcol h4{font-size:6px;font-weight:400;color:#aaa;margin-bottom:2px}
.hours{position:absolute;left:847px;top:60px;width:153px;height:32px;border:1px solid #777;border-radius:3px;font-size:8px;line-height:10px;padding:5px 8px;font-weight:600}
.mission{position:absolute;left:847px;top:110px;width:160px;font-size:7.5px;line-height:10px;font-weight:600}
.news{position:absolute;left:316px;top:286px;width:245px;text-align:center;font-size:8px;line-height:10px}
.news-input{position:absolute;left:700px;top:288px;width:153px;height:21px;background:#fff;border-radius:2px;font-size:6px;color:#aaa;padding:6px}
.news-btn{position:absolute;left:860px;top:288px;width:25px;height:21px;background:#3f6ed8;border-radius:3px;display:flex;align-items:center;justify-content:center}

.contacts{top:4407px;left:0;width:1200px;height:48px;background:#fff;font-size:11px;color:var(--ink)}
.contacts div{position:absolute;transform:translateX(-50%);text-align:center;line-height:12px}
.bottom{top:4455px;left:0;width:1200px;height:132px;background:var(--night);color:#ddd}
.social{position:absolute;top:20px;left:194px;display:flex;align-items:center;gap:8px;font-size:8px}
.social i{display:block;width:15px;height:15px;border-radius:50%;background:#eee}
.legal{position:absolute;top:52px;left:194px;font-size:7.5px}
.footer-brand{position:absolute;top:80px;left:196px;display:flex;align-items:center;gap:14px;font-size:22px;letter-spacing:.04em;color:#fff}
.footer-brand .dot{width:30px;height:30px;border-radius:50%;background:#fff}
</style>
</head>
<body>

<div class="abs topline"></div>
<header class="abs header">
  <div class="abs brand" style="left:196px;top:13px"><span class="dot"></span>BRIGHTWELL PRECIOUS METALS REFINERIES</div>
  <div class="abs search">Search for products or categories...</div>
  <svg class="abs icon" style="left:913px;top:13px" width="15" height="15" viewBox="0 0 16 16"><circle cx="8" cy="8" r="7" fill="none" stroke="#1c1b1b" stroke-width="1.4"/><circle cx="8" cy="6.3" r="2.3" fill="#1c1b1b"/><path d="M3.8 12.6c1-2 2.4-2.8 4.2-2.8s3.2.8 4.2 2.8" fill="#1c1b1b"/></svg>
  <svg class="abs icon" style="left:950px;top:12px" width="13" height="17" viewBox="0 0 12 16"><path d="M6 0C2.7 0 0 2.6 0 5.9 0 10.3 6 16 6 16s6-5.7 6-10.1C12 2.6 9.3 0 6 0z" fill="#1c1b1b"/><circle cx="6" cy="6" r="2.2" fill="#fff"/></svg>
  <div class="abs callbtn"><svg width="14" height="14" viewBox="0 0 24 24"><path d="M6.6 10.8a15.2 15.2 0 006.6 6.6l2.2-2.2c.3-.3.7-.4 1-.2 1.1.4 2.3.6 3.6.6.6 0 1 .4 1 1V20c0 .6-.4 1-1 1A17 17 0 013 4c0-.6.4-1 1-1h3.5c.6 0 1 .4 1 1 0 1.3.2 2.5.6 3.6.1.3 0 .7-.2 1z" fill="#fff"/></svg></div>
</header>
<nav class="abs nav">
  <a style="left:244px">Gold</a><a style="left:345px">Silver</a><a style="left:447px">Shop All</a>
  <a style="left:550px">Deals<span class="badge"></span></a><a style="left:650px">Sell to us</a>
  <a style="left:751px">We Buy</a><a style="left:853px">IRA</a><a style="left:954px">Jewelry</a>
</nav>

<section class="abs hero">
  <div class="hero-media" role="img" aria-label="Molten gold being poured from a glowing crucible"></div>
  <h1 class="abs hero-title">Refinery<br>Process</h1>
</section>

<section class="abs about">
  <div class="abs center" style="top:96px"><div class="rule-orn"></div></div>
  <h2 class="abs center" style="top:128px;font-size:21px">About Our Precious Metal Refinery</h2>
  <div class="abs copy" style="top:172px;left:295px;width:610px;text-align:center">
    <p>Most refineries are set up to work on precious metals behind closed doors. Here at Brightwell VKS we not only invite you to witness your lot being melted; we encourage you to watch every step of your metals being processed. We have a comfortable waiting area with bulletproof walls and windows for you to witness the melting as it is taking place.</p>
    <p>Our precious metal refinery is equipped with the latest technology and state of the art assaying equipment used to test each lot of your precious metals, ensuring your results are both accurate and precise.</p>
    <p>You will receive an analysis of your metals; certifying the results and giving you peace of mind.</p>
    <p>We take pride in our timeliness and efficiency. We know that time is money and your time is valuable; we will give you your one-day settlement in a matter of hours, with your choice of cash, check or wire transfer. Please call ahead and schedule a same-day appointment at our facility.</p>
  </div>
</section>

<div class="abs video" role="img" aria-label="Video: a freshly poured gold bar on a dark refinery floor">
  <div class="play"><svg width="18" height="20" viewBox="0 0 18 20"><path d="M2 1l15 9-15 9z" fill="#111"/></svg></div>
</div>

<section>
  <div class="abs center" style="top:1461px"><div class="rule-orn"></div></div>
  <h2 class="abs center" style="top:1500px;font-size:21px">Personal Relationships</h2>
  <div class="abs copy" style="top:1543px;left:295px;width:610px;text-align:center">
    <p>We at Brightwell Precious Metals Refineries recognize the value of personal relationships and the details that take service from good to great. We strive to build a personal relationship with our clients. By gaining your confidence and giving consistent accurate results, we work diligently to earn your trust. Ensuring our client's complete satisfaction is our number one goal.</p>
    <p>Brightwell Precious Metals Refineries is built on the idea that trust is the most important asset to a successful business. We strive to earn your trust and confidence every day through transparency, accuracy and personal relationships with each and every client. We recognize that trust is valuable and we at Brightwell VKS want to earn yours.</p>
    <p>Trust can only be earned; give us the opportunity to serve you.</p>
  </div>
  <div class="abs gems">
    <div class="gem" style="left:257px;background:linear-gradient(180deg,#dfe3d6,#5f7a55 60%,#2e4a2c)" role="img" aria-label="Evergreen forest"></div>
    <div class="gem" style="left:440px;background:radial-gradient(circle at 50% 45%,#f0b13a,#6e4a14 50%,#1a1410)" role="img" aria-label="Gold refining in a crucible"></div>
    <div class="gem" style="left:620px;background:linear-gradient(135deg,#d9d9d9,#6d6d6d 50%,#1f1f1f)" role="img" aria-label="Minted silver bars"></div>
    <div class="gem" style="left:798px;background:linear-gradient(135deg,#2b1a14,#b2491c 55%,#f3a04a)" role="img" aria-label="Market chart on a screen"></div>
    <div class="gem-label" style="left:328px">CORPORATE RESPONSIBILITY</div>
    <div class="gem-label" style="left:511px">REFINING</div>
    <div class="gem-label" style="left:691px">MINTING</div>
    <div class="gem-label" style="left:869px">NEWS &amp; EVENTS</div>
  </div>
</section>

<section class="abs middle">
  <div class="middle-photo" role="img" aria-label="Refiner in protective gloves stirring molten metal in a crucible"></div>
  <div class="abs" style="left:855px;top:141px"><div class="rule-orn"></div></div>
  <h2 class="abs" style="left:600px;width:600px;text-align:center;top:184px">No Middle-Man</h2>
  <div class="abs hr" style="top:230px"></div>
  <div class="abs copy" style="left:735px;width:330px;top:254px;text-align:center">At Brightwell Precious Metals we melt gold and silver received from buying gold and authorized dealers such as pawn shops and we buy gold places. Doesn't it make sense to cut them out? Deal direct with us, we're confident you'll walk out happy!</div>
  <div class="abs scroll-track" style="top:235px;height:38px"></div>
  <div class="abs scroll-track" style="top:285px;height:38px;background:#fff"></div>
  <div class="abs scroll-track" style="top:335px;height:38px"></div>
</section>
<div class="coin gold" style="left:702px" role="img" aria-label="Gold bullion coin"></div>
<div class="coin silver" style="left:807px" role="img" aria-label="Silver bullion coin"></div>
<div class="coin gold" style="left:910px" role="img" aria-label="Gold bullion coin"></div>
<div class="coin silver" style="left:1015px" role="img" aria-label="Silver bullion coin"></div>

<section>
  <div class="abs center" style="top:2632px"><div class="rule-orn"></div></div>
  <h2 class="abs center reg-title" style="top:2670px">Wholesale Registration</h2>
  <div class="dash" style="left:314px;width:108px"></div>
  <div class="dash" style="left:469px;width:108px"></div>
  <div class="dash" style="left:624px;width:108px"></div>
  <div class="dash" style="left:779px;width:108px"></div>
  <div class="step active" style="left:290px"><svg width="14" height="16" viewBox="0 0 14 16"><path d="M1 1h8l4 4v10H1z" fill="#fff"/><path d="M3 8h8M3 11h8" stroke="#1c1b1b"/></svg></div>
  <div class="step" style="left:445px"><svg width="14" height="16" viewBox="0 0 14 16"><circle cx="7" cy="5" r="3.5" fill="#1c1b1b"/><path d="M0 16c0-4 3-6 7-6s7 2 7 6z" fill="#1c1b1b"/></svg></div>
  <div class="step" style="left:600px"><svg width="14" height="16" viewBox="0 0 14 16"><circle cx="7" cy="5" r="3.5" fill="#1c1b1b"/><path d="M0 16c0-4 3-6 7-6s7 2 7 6z" fill="#1c1b1b"/></svg></div>
  <div class="step" style="left:755px"><svg width="12" height="16" viewBox="0 0 12 16"><rect x="0" y="0" width="12" height="16" rx="1" fill="#1c1b1b"/><path d="M3 4h6M3 7h6M3 10h6" stroke="#fff"/></svg></div>
  <div class="step" style="left:910px"><svg width="18" height="13" viewBox="0 0 18 13"><path d="M0 1h11v9H0zM11 4h4l3 3v3h-7z" fill="#1c1b1b"/><circle cx="4" cy="11" r="2" fill="#1c1b1b"/><circle cx="14" cy="11" r="2" fill="#1c1b1b"/></svg></div>
  <div class="step-label" style="left:290px">Business Contact<br>Information</div>
  <div class="step-label" style="left:445px">Primary Owner<br>or Principal</div>
  <div class="step-label" style="left:600px">Secondary Owner<br>or Principal</div>
  <div class="step-label" style="left:755px">Billing</div>
  <div class="step-label" style="left:910px">Shipping</div>

  <h3 class="abs center" style="top:2897px;font-size:20px">Business Contact Information</h3>

  <div class="form-label" style="left:198px;top:2953px">Legal Business Name<b>*</b></div>
  <div class="form-label" style="left:470px;top:2953px">Company Phone<b>*</b></div>
  <div class="form-label" style="left:742px;top:2953px">Email<b>*</b></div>
  <div class="field" style="left:198px;top:2969px;width:259px"></div>
  <div class="field" style="left:470px;top:2969px;width:260px"></div>
  <div class="field" style="left:742px;top:2969px;width:260px"></div>

  <div class="form-label" style="left:198px;top:3026px">Company Physical Address<b>*</b></div>
  <div class="form-label" style="left:470px;top:3026px">City<b>*</b></div>
  <div class="form-label" style="left:573px;top:3026px">State<b>*</b></div>
  <div class="form-label" style="left:650px;top:3026px">Zip<b>*</b></div>
  <div class="form-label" style="left:742px;top:3026px">Federal ID/EIN#<b>*</b></div>
  <div class="field" style="left:198px;top:3043px;width:259px"></div>
  <div class="field" style="left:470px;top:3043px;width:79px"></div>
  <div class="field" style="left:561px;top:3043px;width:78px"></div>
  <div class="field" style="left:650px;top:3043px;width:80px"></div>
  <div class="field" style="left:742px;top:3043px;width:260px"></div>

  <div class="form-label" style="left:198px;top:3100px">Date Business Commenced<b>*</b></div>
  <div class="form-label" style="left:470px;top:3100px">Business Type<b>*</b></div>
  <div class="form-label" style="left:742px;top:3100px">Website<b>*</b></div>
  <div class="field" style="left:198px;top:3117px;width:259px"></div>
  <div class="field" style="left:470px;top:3117px;width:260px"><svg class="abs" style="right:12px;top:16px" width="8" height="5" viewBox="0 0 8 5"><path d="M1 1l3 3 3-3" fill="none" stroke="#333"/></svg></div>
  <div class="field" style="left:742px;top:3117px;width:260px"></div>

  <div class="abs continue">Continue <svg width="9" height="8" viewBox="0 0 9 8"><path d="M0 4h8M5 1l3 3-3 3" fill="none" stroke="#fff"/></svg></div>
</section>

<section>
  <div class="abs center" style="top:3276px"><div class="rule-orn"></div></div>
  <h2 class="abs center" style="top:3312px;font-size:21px">Industires We Serve</h2>
  <div class="card" style="left:-92px;background:linear-gradient(160deg,#d8dbe0,#8c8f95 60%,#3d3f44)" role="img" aria-label="Financial advisors meeting with a client"><div class="shade"></div><span style="left:94px">Advisors</span></div>
  <div class="card" style="left:187px;background:linear-gradient(160deg,#c7c2bc,#6f6a66 55%,#2b2a2a)" role="img" aria-label="Estate attorney reviewing documents"><div class="shade"></div><span>Estate Attorneys</span></div>
  <div class="card" style="left:466px;background:linear-gradient(160deg,#c9d6e0,#6f8aa3 55%,#2d3f55)" role="img" aria-label="Dentists in scrubs and gloves"><div class="shade"></div><span>Dentists</span></div>
  <div class="card" style="left:746px;background:linear-gradient(180deg,#e6e3df,#a59a8a 50%,#4a443d)" role="img" aria-label="Jewelry store interior with display cases"><div class="shade"></div><span>Jewelry Stores</span></div>
  <div class="card" style="left:1025px;background:linear-gradient(160deg,#d6e1ea,#7b97ad 55%,#2f4455)" role="img" aria-label="Dental practice treatment room"><div class="shade"></div><span>Dental Practices</span></div>
  <div class="arrow" style="left:121px"><svg width="8" height="8" viewBox="0 0 8 8"><path d="M3 1l3 3-3 3" fill="none" stroke="#fff" stroke-width="1.3"/></svg></div>
  <div class="arrow" style="left:402px"><svg width="8" height="8" viewBox="0 0 8 8"><path d="M3 1l3 3-3 3" fill="none" stroke="#fff" stroke-width="1.3"/></svg></div>
  <div class="arrow hot" style="left:682px"><svg width="8" height="8" viewBox="0 0 8 8"><path d="M3 1l3 3-3 3" fill="none" stroke="#1c1b1b" stroke-width="1.3"/></svg></div>
  <div class="arrow" style="left:961px"><svg width="8" height="8" viewBox="0 0 8 8"><path d="M3 1l3 3-3 3" fill="none" stroke="#fff" stroke-width="1.3"/></svg></div>
  <div class="pager" style="left:527px"></div>
  <div class="pager on" style="left:578px"></div>
  <div class="pager" style="left:630px"></div>

  <div class="perk dark" style="left:215px">
    <h3>Price match guarantee</h3><p>On all bullion products.</p><div class="cta">LEARN MORE</div>
    <svg class="mark" width="24" height="24" viewBox="0 0 24 24"><circle cx="12" cy="12" r="10" fill="none" stroke="#e4b75c" stroke-width="1.5"/><path d="M7 12l3.5 3.5L17 9" fill="none" stroke="#e4b75c" stroke-width="1.5"/></svg>
  </div>
  <div class="perk goldcard" style="left:477px">
    <h3 style="font-weight:500">100% Insured</h3><p>All orders are tracked, insured, and<br>require a signature.</p>
    <svg class="mark" width="22" height="24" viewBox="0 0 22 24"><path d="M11 1l9 3v7c0 6-4 10-9 12C6 21 2 17 2 11V4z" fill="none" stroke="#1c1b1b" stroke-width="1.4"/><path d="M7 12l3 3 5-6" fill="none" stroke="#1c1b1b" stroke-width="1.4"/></svg>
  </div>
  <div class="perk dark" style="left:739px">
    <h3>Free Shipping</h3><p>Orders ship free over $399.</p><div class="cta">SHOP NOW</div>
    <svg class="mark" width="26" height="20" viewBox="0 0 26 20"><path d="M1 2h15v12H1zM16 6h5l4 4v4h-9z" fill="none" stroke="#e4b75c" stroke-width="1.4"/><circle cx="6" cy="16" r="2.3" fill="none" stroke="#e4b75c" stroke-width="1.4"/><circle cx="20" cy="16" r="2.3" fill="none" stroke="#e4b75c" stroke-width="1.4"/></svg>
  </div>
</section>

<footer class="abs footer">
  <div class="fcol" style="left:199px"><h4>Buying &amp; selling</h4>Shop Bullion<br>IRA Rollovers<br>Silver Bullion<br>Gold Bullion<br>Platinum Bullion<br>Palladium Bullion<br>Brightwell Jewelry</div>
  <div class="fcol" style="left:361px"><h4>Company</h4>Leave a Review<br>Testimonials<br>Refinery Process<br>Blog<br>About Us</div>
  <div class="fcol" style="left:523px"><h4>Customer care</h4>My account<br>Investment Tools<br>Contact us<br>FAQs<br>Jewelry 101<br>Jewelry Repair</div>
  <div class="fcol" style="left:685px"><h4>Legal</h4>Privacy Policy<br>Terms and Conditions<br>Mail-in Terms<br>Acceptable Use<br>Cookie Policy<br>Disclaimer Policy<br>Payment Terms<br>Shipping Policy<br>Returns Policy<br>Price Match<br>Affiliate Program Terms of Use</div>
  <div class="hours">Open Mon-Fri<br>10:00a - 6:00p PST</div>
  <div class="mission">Brightwell Precious Metals Refineries is a proudly patriotic Christian business in the United States of America.</div>
  <svg class="abs" style="left:849px;top:160px" width="12" height="18" viewBox="0 0 12 18"><path d="M5 0h2v5h5v2H7v11H5V7H0V5h5z" fill="#fff"/></svg>
  <div class="abs" style="left:880px;top:161px;width:40px;height:18px;background:linear-gradient(180deg,#c8334a 0,#c8334a 50%,#e9e9e9 50%);border-radius:2px" role="img" aria-label="National flag"></div>
  <div class="news">Subscribe to our newsletter to be the first to know about special deals and promotions.</div>
  <div class="news-input">Enter Email</div>
  <div class="news-btn"><svg width="10" height="8" viewBox="0 0 10 8"><rect x=".5" y=".5" width="9" height="7" fill="none" stroke="#fff"/><path d="M.5 .5l4.5 4 4.5-4" fill="none" stroke="#fff"/></svg></div>
</footer>

<div class="abs contacts">
  <div style="left:326px;top:18px">(555) 014-2270</div>
  <div style="left:598px;top:12px">2140 Larchmont Ave NE,<br>Fairview, OR 97000</div>
  <div style="left:872px;top:18px">info@brightwellvks.example</div>
</div>

<div class="abs bottom">
  <div class="social">Follow us on social media to stay up to date: <i></i><i></i><i></i><i></i><i></i></div>
  <div class="legal">© 2025 All Rights Reserved Brightwell Precious Metals Refineries</div>
  <div class="footer-brand"><span class="dot"></span>BRIGHTWELL PRECIOUS METALS REFINERIES</div>
</div>

</body>
</html>
```